Bref créative
Business cards and stationery for investment company
Velorin Holdings
Professional
Owen Pellick
P.O. Box YYY
Brenford, Calver 84219
owen.pellick@velorin.example
www.velorin.example
Logo only

```html
<!DOCTYPE html>
<html lang="en">
<head>
<meta charset="utf-8">
<title>Velorin Holdings Stationery</title>
<link href="https://fonts.googleapis.com/css2?family=Open+Sans:wght@400;600;700&display=swap" rel="stylesheet">
<style>
  :root {
    --red: #c8101e;
    --red-dark: #8e0a14;
    --paper: #ffffff;
    --paper-shade: #ececec;
    --ink: #333333;
    --ink-soft: #777777;
    --grey-flap: #6e6e6e;
    --bg-light: #8a8a8a;
    --bg-dark: #3c3c3c;
  }
  * { box-sizing: border-box; margin: 0; padding: 0; }
  html, body { width: 1200px; height: 437px; overflow: hidden; }
  body {
    font-family: "Open Sans", Arial, sans-serif;
    color: var(--ink);
    background: radial-gradient(ellipse at 50% 45%, var(--bg-light) 0%, #626262 55%, var(--bg-dark) 100%);
    position: relative;
  }
  .piece { position: absolute; background: var(--paper); box-shadow: 0 3px 8px rgba(0,0,0,.45); overflow: hidden; }
  .piece svg.shape { position: absolute; inset: 0; width: 100%; height: 100%; }
  .brand { position: absolute; font-weight: 700; color: var(--red); white-space: nowrap; }

  /* business cards */
  .card { left: 28px; width: 126px; height: 76px; }
  .card-front { top: 130px; }
  .card-front .brand { top: 8px; right: 10px; font-size: 9px; }
  .card-front .person { position: absolute; top: 22px; right: 10px; text-align: right; font-size: 5px; line-height: 1.3; }
  .card-front .person strong { font-size: 6px; display: block; }
  .card-front .contact { position: absolute; bottom: 6px; right: 8px; text-align: right; font-size: 4px; line-height: 1.35; color: var(--ink-soft); }
  .card-back { top: 216px; background: linear-gradient(135deg, #fafafa, var(--paper-shade)); }
  .card-back .brand { top: 22px; left: 12px; font-size: 22px; color: #d9d9d9; }
  .card-mark { top: 302px; }
  .card-mark .brand { top: 28px; left: 26px; font-size: 15px; }

  /* letterheads */
  .letter { top: 24px; width: 228px; height: 389px; }
  .letter-one { left: 170px; }
  .letter-two { left: 460px; }
  .letter .brand { top: 10px; left: 0; right: 0; text-align: center; font-size: 11px; }
  .letter .body { position: absolute; top: 70px; left: 22px; right: 22px; font-size: 4.6px; line-height: 1.55; }
  .letter .address { margin-bottom: 10px; }
  .letter .address strong { font-size: 5.5px; }
  .letter p { margin-bottom: 6px; text-align: justify; }
  .letter .sign { margin-top: 14px; }
  .letter .sign .name { font-size: 8px; font-style: italic; color: #555; margin: 6px 0 2px; }
  .letter .footer { position: absolute; bottom: 6px; right: 12px; font-size: 4px; color: #fff; text-align: right; line-height: 1.4; }
  .letter-two .body { top: 64px; }

  /* envelopes */
  .envelope { left: 860px; width: 310px; }
  .env-top { top: 36px; height: 96px; }
  .env-top .brand { top: 8px; left: 0; right: 0; text-align: center; font-size: 12px; color: #fff; }
  .env-flap { top: 128px; height: 100px; background: var(--paper-shade); }
  .env-flap .brand { top: 14px; left: 0; right: 0; text-align: center; font-size: 12px; color: #fff; }
  .env-front { top: 222px; height: 114px; }
  .env-front .brand { top: 24px; left: 0; right: 0; text-align: center; font-size: 13px; }
  .signoff { position: absolute; left: 1100px; top: 352px; width: 80px; text-align: center; }
  .signoff .brand { position: static; font-size: 14px; display: block; }
  .signoff small { font-size: 5px; color: #ddd; display: block; }
</style>
</head>
<body>

<section class="piece card card-front">
  <svg class="shape" viewBox="0 0 126 76" preserveAspectRatio="none" aria-hidden="true">
    <path d="M0 0 H26 C12 30 18 58 46 76 H0 Z" fill="var(--red)"/>
    <path d="M26 0 C12 30 18 58 46 76" fill="none" stroke="var(--red-dark)" stroke-width="2"/>
  </svg>
  <span class="brand">Velorin</span>
  <div class="person"><strong>Owen Pellick</strong>President</div>
  <div class="contact">P.O. Box YYY<br>Brenford, Calver 84219<br>owen.pellick@velorin.example<br>www.velorin.example</div>
</section>

<section class="piece card card-back">
  <span class="brand">Velorin</span>
</section>

<section class="piece card card-mark">
  <svg class="shape" viewBox="0 0 126 76" preserveAspectRatio="none" aria-hidden="true">
    <path d="M0 60 C40 50 80 70 126 52 V76 H0 Z" fill="var(--red)"/>
  </svg>
  <span class="brand">Velorin</span>
</section>

<article class="piece letter letter-one">
  <svg class="shape" viewBox="0 0 228 389" preserveAspectRatio="none" aria-hidden="true">
    <path d="M0 0 H228 V16 C160 40 60 30 0 52 Z" fill="var(--paper-shade)"/>
    <path d="M0 340 C70 320 150 360 228 330 V389 H0 Z" fill="var(--red)"/>
    <path d="M0 352 C80 332 150 372 228 344" fill="none" stroke="var(--red-dark)" stroke-width="3"/>
  </svg>
  <span class="brand">Velorin</span>
  <div class="body">
    <div class="address"><strong>Recipient Name</strong><br>100 Main Street<br>City, State 00000</div>
    <p>Dear Partner,</p>
    <p>We appreciate your continued interest in our investment programs. This letter confirms the details discussed during our recent meeting and outlines the next steps for your portfolio review. Please contact our office with any questions regarding the enclosed summary.</p>
    <p>Our team remains committed to careful planning, clear reporting and steady long term growth for every client we serve.</p>
    <div class="sign">Sincerely,<div class="name">Owen Pellick</div>President</div>
  </div>
  <div class="footer">P.O. Box YYY, Brenford, Calver 84219<br>www.velorin.example</div>
</article>

<article class="piece letter letter-two">
  <svg class="shape" viewBox="0 0 228 389" preserveAspectRatio="none" aria-hidden="true">
    <path d="M150 0 H228 V40 C200 20 175 10 150 0 Z" fill="var(--red)"/>
    <path d="M0 330 C60 350 150 320 228 340 V389 H0 Z" fill="var(--red)"/>
    <path d="M0 320 C60 342 150 310 228 330" fill="none" stroke="#cccccc" stroke-width="3"/>
  </svg>
  <span class="brand">Velorin</span>
  <div class="body">
    <div class="address"><strong>Recipient Name</strong><br>100 Main Street<br>City, State 00000</div>
    <p>Dear Partner,</p>
    <p>We appreciate your continued interest in our investment programs. This letter confirms the details discussed during our recent meeting and outlines the next steps for your portfolio review. Please contact our office with any questions regarding the enclosed summary.</p>
    <p>Our team remains committed to careful planning, clear reporting and steady long term growth for every client we serve.</p>
    <div class="sign">Sincerely,<div class="name">Owen Pellick</div>President</div>
  </div>
  <div class="footer">P.O. Box YYY, Brenford, Calver 84219<br>www.velorin.example</div>
</article>

<section class="piece envelope env-top">
  <svg class="shape" viewBox="0 0 310 96" preserveAspectRatio="none" aria-hidden="true">
    <path d="M0 0 H310 V16 L155 50 L0 16 Z" fill="var(--red)"/>
    <path d="M0 96 L135 42 M310 96 L175 42" stroke="#dddddd" stroke-width="1" fill="none"/>
  </svg>
  <span class="brand">Velorin</span>
</section>

<section class="piece envelope env-flap">
  <svg class="shape" viewBox="0 0 310 100" preserveAspectRatio="none" aria-hidden="true">
    <path d="M0 0 H310 L155 66 Z" fill="var(--grey-flap)"/>
    <path d="M0 100 L155 60 L310 100" stroke="#d0d0d0" stroke-width="1" fill="none"/>
  </svg>
  <span class="brand">Velorin</span>
</section>

<section class="piece envelope env-front">
  <svg class="shape" viewBox="0 0 310 114" preserveAspectRatio="none" aria-hidden="true">
    <path d="M0 0 L155 60 L310 0" stroke="#e2e2e2" stroke-width="1" fill="none"/>
    <path d="M0 84 C28 80 50 92 70 114 H0 Z" fill="var(--red)"/>
  </svg>
  <span class="brand">Velorin</span>
</section>

<div class="signoff"><span class="brand">Velorin</span><small>Velorin Holdings</small></div>

</body>
</html>
```